Copper Lattice of Brave Movers

Hi - I would like your help transforming my (terrible) drawing into a graphic that pops -using hex colors I'll give you - so that I can put it into stationary and on t-shirts or tote bags. My company, the Tundrel Institute, trains social change leaders (from the sectors in the periodic table) on how to lead large-scale change. I have this vision - the "periodic table" but these are the sectors that my clients work in. If you are having trouble reading my writing, I apologize. Our hex colors are: #114769, #76984C, #80B5CF (Seagull), #8F2C63 and Rangoon Black #191919. You don't need to use all of them, but it'd be good to be consistent with our overall branding. If you can't read my writing, I will send correct spelling. The "Tundrel" with the flowers on the bottom is for a separate design bid.

Target Market(s)

nonprofit, social entrepreneurs, philanthropy, leaders

Requirements
Must have
• clean, readable font. alignment to look like periodic table of elements. heart icon for love, cat face for cats.

```html
<!DOCTYPE html>
<html lang="en">
<head>
<meta charset="utf-8">
<title>Copper Lattice of Brave Movers</title>
<link href="https://fonts.googleapis.com/css2?family=Roboto+Condensed:wght@700&family=Arimo:wght@700&display=swap" rel="stylesheet">
<style>
  :root {
    --navy: #114769;
    --seagull: #80B5CF;
    --leaf: #86C342;
    --paper: #FFFFFF;
    --tile-w: 143px;
    --tile-h: 138px;
  }
  html, body {
    margin: 0;
    padding: 0;
    overflow: hidden;
    background: var(--paper);
  }
  .canvas {
    position: relative;
    width: 1200px;
    height: 1000px;
    background: var(--paper);
    overflow: hidden;
  }
  .element {
    position: absolute;
    width: var(--tile-w);
    height: var(--tile-h);
    box-sizing: border-box;
    color: var(--paper);
  }
  .element--navy { background: var(--navy); }
  .element--leaf { background: var(--leaf); }
  .element--seagull { background: var(--seagull); color: var(--navy); }
  .element__name {
    position: absolute;
    left: 12px;
    top: 12px;
    right: 4px;
    margin: 0;
    font-family: "Roboto Condensed", "Arial Narrow", sans-serif;
    font-weight: 700;
    font-size: 23px;
    line-height: 27px;
    letter-spacing: 0.1px;
  }
  .element__symbol {
    position: absolute;
    left: 28px;
    top: 76px;
    margin: 0;
    font-family: "Arimo", Arial, sans-serif;
    font-weight: 700;
    font-size: 44px;
    line-height: 44px;
  }
  .element__icon {
    position: absolute;
    left: 38px;
    top: 76px;
  }
  .value-row .element__name { top: 12px; left: 14px; }
  .value-row .element__symbol { top: 82px; }
</style>
</head>
<body>
<main class="canvas" aria-label="Copper Lattice of Brave Movers">

  <!-- Row 1 -->
  <div class="element element--navy" style="left:152px;top:135px">
    <p class="element__name">Violence<br>Prevention</p><p class="element__symbol">Vp</p>
  </div>
  <div class="element element--leaf" style="left:911px;top:135px">
    <p class="element__name">Belonging</p><p class="element__symbol">B</p>
  </div>

  <!-- Row 2 -->
  <div class="element element--seagull" style="left:152px;top:284px">
    <p class="element__name">Early<br>Childhood</p><p class="element__symbol">Ec</p>
  </div>
  <div class="element element--seagull" style="left:304px;top:284px">
    <p class="element__name">Climate<br>Change</p><p class="element__symbol">Cc</p>
  </div>
  <div class="element element--seagull" style="left:456px;top:284px">
    <p class="element__name">Enviromental<br>Justice</p><p class="element__symbol">Ej</p>
  </div>
  <div class="element element--navy" style="left:608px;top:284px">
    <p class="element__name">Human<br>Services</p><p class="element__symbol">Hs</p>
  </div>
  <div class="element element--leaf" style="left:760px;top:284px">
    <p class="element__name">Health<br>Care</p><p class="element__symbol">Hc</p>
  </div>
  <div class="element element--leaf" style="left:911px;top:284px">
    <p class="element__name">Housing</p><p class="element__symbol">H</p>
  </div>

  <!-- Row 3 -->
  <div class="element element--navy" style="left:152px;top:432px">
    <p class="element__name">Education</p><p class="element__symbol">Ed</p>
  </div>
  <div class="element element--seagull" style="left:304px;top:432px">
    <p class="element__name">After<br>School</p><p class="element__symbol">As</p>
  </div>
  <div class="element element--seagull" style="left:456px;top:432px">
    <p class="element__name">Social<br>Justice</p><p class="element__symbol">Sj</p>
  </div>
  <div class="element element--seagull" style="left:608px;top:432px">
    <p class="element__name">Civil<br>Rights</p><p class="element__symbol">Cr</p>
  </div>
  <div class="element element--seagull" style="left:760px;top:432px">
    <p class="element__name">Health<br>Equity</p><p class="element__symbol">He</p>
  </div>
  <div class="element element--leaf" style="left:911px;top:432px">
    <p class="element__name">Jobs</p><p class="element__symbol">Jo</p>
  </div>

  <!-- Row 4 -->
  <div class="element element--leaf" style="left:152px;top:581px">
    <p class="element__name">Democracy</p><p class="element__symbol">D</p>
  </div>
  <div class="element element--leaf" style="left:304px;top:581px">
    <p class="element__name">Animal<br>Welfare</p>
    <svg class="element__icon" width="64" height="54" viewBox="0 0 64 54" role="img" aria-label="Cat face icon">
      <rect x="8" y="4" width="48" height="46" rx="12" fill="#FFFFFF"/>
    </svg>
  </div>
  <div class="element element--seagull" style="left:456px;top:581px">
    <p class="element__name">Racial<br>Justice</p><p class="element__symbol">Rj</p>
  </div>
  <div class="element element--navy" style="left:608px;top:581px">
    <p class="element__name">Immigrant<br>Rights</p><p class="element__symbol">Ir</p>
  </div>
  <div class="element element--leaf" style="left:760px;top:581px">
    <p class="element__name">Behavioral<br>Health</p><p class="element__symbol">Bh</p>
  </div>
  <div class="element element--navy" style="left:911px;top:581px">
    <p class="element__name">Inter-<br>generational</p><p class="element__symbol">Ig</p>
  </div>

  <!-- Values row -->
  <div class="value-row">
    <div class="element element--leaf" style="left:231px;top:733px;width:142px">
      <p class="element__name">Love</p>
      <svg class="element__icon" style="left:37px;top:72px" width="50" height="46" viewBox="0 0 50 46" role="img" aria-label="Heart icon">
        <path d="M25 44 C10 32 1 24 1 13 C1 6 7 1 13.5 1 C19 1 23 4 25 8 C27 4 31 1 36.5 1 C43 1 49 6 49 13 C49 24 40 32 25 44 Z" fill="#FFFFFF"/>
      </svg>
    </div>
    <div class="element element--leaf" style="left:381px;top:733px;width:142px">
      <p class="element__name">Authenticity</p><p class="element__symbol">A</p>
    </div>
    <div class="element element--leaf" style="left:531px;top:733px;width:142px">
      <p class="element__name">Humility</p><p class="element__symbol">Hu</p>
    </div>
    <div class="element element--leaf" style="left:681px;top:733px;width:142px">
      <p class="element__name">Audacity</p><p class="element__symbol">Au</p>
    </div>
    <div class="element element--seagull" style="left:832px;top:733px;width:142px">
      <p class="element__name">Integrity</p><p class="element__symbol">I</p>
    </div>
  </div>

</main>
</body>
</html>
```